4K Business Card Design

We need a business card that emphasizes consulting services worldwide. The name of the company is KKKK Consulting Group. We provide consulting services across several industries including but not limited to commodities, telecom, manufacturing, logistics, marketing and operations. We would like to see a creative design that emphasizes the global aspect, including Latin America and US markets, as well the bilingual nature of the service offerings.

The contact information section should include icons to represent the following data:
1) Name, Title and Company Name
2) Mobile Number
3) Skype ID
4) Email
5) Web Page
6) Location

We would like to see a card that emphasizes the worldwide concept. The back of the card should be simple, including only the logo (or a portion of the logo) and the slogan.

We would also like to see business cards in a booklet format. The colors to be used should be the same combination of colors used in the logos attached to this brief.

The logo design and some business card examples from Artful Herd are attached for reference on style and look.

Target Market(s)

International business executives, 45-65 years of age, bilingual

Industry/Entity Type

Marketing

Colors
0792cd
34a7d8
85cae6
ffffff
cee9f5
ecf7fb

Requirements
Must have
• Please follow colors in logo attached.

2) Mobile Number
3) Skype ID
4) Email
5) Web Page
6) Location
Nice to have
• Global concept, consulting profile, diverse industry focus
Should not have
• No black color

```html
<!DOCTYPE html>
<html lang="en">
<head>
<meta charset="utf-8">
<title>KKKK Consulting Group – Business Card</title>
<link rel="stylesheet" href="https://fonts.googleapis.com/css2?family=Questrial&family=Open+Sans:wght@400;700&display=swap">
<style>
  :root {
    --blue-deep: #0792cd;
    --blue-mid: #34a7d8;
    --blue-soft: #85cae6;
    --blue-pale: #cee9f5;
    --blue-mist: #ecf7fb;
    --white: #ffffff;
    --slate: #4f6470;
    --stage: #eef1f3;
  }
  * { box-sizing: border-box; margin: 0; padding: 0; }
  html, body { width: 1200px; height: 800px; overflow: hidden; }
  body { background: var(--stage); font-family: "Questrial", sans-serif; position: relative; }

  .card { position: absolute; overflow: hidden; box-shadow: 0 10px 28px rgba(40, 70, 90, .18); }

  /* Back of card */
  .card-back {
    left: 90px; top: 85px; width: 360px; height: 630px;
    background: linear-gradient(160deg, var(--blue-soft) 0%, #6dbbe0 100%);
  }
  .card-back .world-map {
    position: absolute; left: 30px; top: 40px; width: 300px; height: 550px;
    border-radius: 40px;
    background: radial-gradient(ellipse at 50% 45%, rgba(52,167,216,.45), rgba(52,167,216,0) 70%);
  }
  .card-back .slogan {
    position: absolute; left: 30px; top: 110px;
    writing-mode: vertical-rl;
    color: var(--white); font-size: 21px; letter-spacing: 1px; line-height: 1;
  }
  .card-back .brand {
    position: absolute; left: 112px; top: 90px; height: 450px;
    writing-mode: vertical-rl;
    text-align: center;
    color: var(--white);
    font-size: 42px; letter-spacing: 2px; line-height: 1.25;
  }
  .card-back .brand-sub { font-size: 32px; letter-spacing: 4px; }
  .card-back .mark {
    position: absolute; left: 232px; top: 280px;
    color: var(--white); font-size: 60px; line-height: 1;
  }

  /* Front of card */
  .card-front {
    left: 500px; top: 220px; width: 630px; height: 360px;
    background: var(--white);
  }
  .card-front .panel { position: absolute; inset: 0; }
  .card-front .mark {
    position: absolute; left: 28px; top: 14px;
    font-size: 96px; line-height: 1; color: var(--blue-soft);
  }
  .card-front .wordmark {
    position: absolute; right: 30px; top: 40px; text-align: right;
    color: var(--slate); font-size: 40px; line-height: 1.05; letter-spacing: 1px;
  }
  .card-front .tagline {
    position: absolute; right: 32px; top: 134px;
    color: var(--blue-deep); font-size: 19px;
  }
  .contact {
    position: absolute; left: 48px; top: 168px;
    font-family: "Open Sans", sans-serif; color: var(--white);
  }
  .contact .name { font-weight: 700; font-size: 18px; letter-spacing: 1px; }
  .contact .title { font-size: 12px; margin-bottom: 10px; color: var(--blue-mist); }
  .contact ul { list-style: none; }
  .contact li { display: flex; align-items: center; gap: 9px; font-size: 13px; line-height: 22px; color: var(--blue-mist); }
  .contact svg { width: 13px; height: 13px; flex: none; }
</style>
</head>
<body>

  <section class="card card-back" aria-label="Back of business card">
    <div class="world-map" role="img" aria-label="Faint world map showing the Americas and global markets"></div>
    <div class="slogan">Consulting Services Worldwide</div>
    <div class="brand">
      <span class="brand-name">KKKK CONSULTING</span><br>
      <span class="brand-sub">GROUP</span>
    </div>
    <div class="mark">4K</div>
  </section>

  <section class="card card-front" aria-label="Front of business card">
    <svg class="panel" viewBox="0 0 630 360" preserveAspectRatio="none" aria-hidden="true">
      <defs>
        <linearGradient id="bandFill" x1="0" y1="0" x2="1" y2="1">
          <stop offset="0" stop-color="#85cae6"/>
          <stop offset="1" stop-color="#5fb3da"/>
        </linearGradient>
      </defs>
      <polygon points="0,120 200,120 630,250 630,360 0,360" fill="url(#bandFill)"/>
      <polygon points="0,0 200,0 200,120 0,120" fill="#cee9f5" opacity=".55"/>
      <line x1="200" y1="120" x2="630" y2="318" stroke="#ffffff" stroke-width="3"/>
      <line x1="200" y1="0" x2="200" y2="120" stroke="#ffffff" stroke-width="2"/>
    </svg>

    <div class="mark">4K</div>
    <div class="wordmark">KKKK CONSULTING<br>GROUP</div>
    <div class="tagline">Consulting Services Worldwide</div>

    <div class="contact">
      <p class="name">ELENA VARGAS</p>
      <p class="title">President &amp; CEO</p>
      <ul>
        <li>
          <svg viewBox="0 0 16 16"><path d="M4 1 L6.5 4.5 L5 6.5 Q7 10 9.5 11 L11.5 9.5 L15 12 L13 15 Q5 14 1 3 Z" fill="#ffffff"/></svg>
          +1 555 014-2290
        </li>
        <li>
          <svg viewBox="0 0 16 16"><rect x="1" y="3" width="14" height="10" fill="#ffffff"/><path d="M1 3 L8 9 L15 3" fill="none" stroke="#85cae6" stroke-width="1.4"/></svg>
          k4cg@postmail.com
        </li>
        <li>
          <svg viewBox="0 0 16 16"><circle cx="8" cy="8" r="7" fill="#ffffff"/></svg>
          k4consultinggroup
        </li>
        <li>
          <svg viewBox="0 0 16 16"><circle cx="8" cy="8" r="6.5" fill="none" stroke="#ffffff" stroke-width="1.4"/><ellipse cx="8" cy="8" rx="3" ry="6.5" fill="none" stroke="#ffffff" stroke-width="1.2"/><line x1="1.5" y1="8" x2="14.5" y2="8" stroke="#ffffff" stroke-width="1.2"/></svg>
          www.kkkkconsulting.com
        </li>
        <li>
          <svg viewBox="0 0 16 16"><path d="M8 15 Q2 8 2 6 A6 6 0 0 1 14 6 Q14 8 8 15 Z" fill="#ffffff"/><circle cx="8" cy="6" r="2" fill="#85cae6"/></svg>
          Bayview, FL
        </li>
      </ul>
    </div>
  </section>

</body>
</html>
```